Business Card *

A business card design
Use the logo uploaded in the brief page.
You may use placeholders in your design layouts.
I will provide the actual business card details to the winning designer.

Logo
Place for contact info (name, title, phone, email, etc)

Requirements
Must have
• Logo

```html
<!DOCTYPE html>
<html lang="en">
<head>
<meta charset="utf-8">
<title>Harrowfield Business Card</title>
<link href="https://fonts.googleapis.com/css2?family=Open+Sans:wght@400;600;700&display=swap" rel="stylesheet">
<style>
  :root {
    --page-bg: #eeeeee;
    --card-dark: #252525;
    --brand-green: #3cb54a;
    --light-green: #8dc63f;
    --logo-grey: #8c8c8c;
    --text-light: #e6e6e6;
    --white: #ffffff;
  }
  html, body {
    margin: 0;
    padding: 0;
    width: 1200px;
    height: 861px;
    overflow: hidden;
    background: var(--page-bg);
    font-family: "Open Sans", sans-serif;
  }
  .canvas {
    position: relative;
    width: 1200px;
    height: 861px;
  }
  .card {
    position: absolute;
    top: 298px;
    width: 430px;
    height: 246px;
    border-radius: 14px;
    background: var(--card-dark);
    overflow: hidden;
    box-shadow: 0 3px 8px rgba(0,0,0,0.25);
  }
  .card--front { left: 144px; }
  .card--back { left: 626px; }

  .brand {
    position: absolute;
    display: flex;
    flex-direction: column;
    align-items: center;
  }
  .brand__dot {
    border-radius: 50%;
    background: var(--brand-green);
  }
  .brand__name {
    font-weight: 700;
    color: var(--logo-grey);
    letter-spacing: 0.5px;
    line-height: 1;
  }
  .card--front .brand {
    left: 0; right: 0; top: 72px;
  }
  .card--front .brand__dot { width: 64px; height: 64px; margin-bottom: 16px; }
  .card--front .brand__name { font-size: 30px; }

  .card--back .brand {
    left: 28px; top: 56px; width: 148px;
  }
  .card--back .brand__dot { width: 46px; height: 46px; margin-bottom: 10px; }
  .card--back .brand__name { font-size: 20px; }

  .card__band {
    position: absolute;
    left: 0; top: 0;
    width: 430px;
    height: 90px;
  }
  .holder {
    position: absolute;
    right: 58px;
    top: 20px;
    text-align: center;
    color: var(--white);
  }
  .holder__name {
    font-size: 18px;
    font-weight: 700;
    line-height: 1.1;
  }
  .holder__title {
    font-size: 9.5px;
    font-weight: 600;
  }
  .contact-list {
    position: absolute;
    left: 29px;
    top: 184px;
    margin: 0;
    padding: 0;
    list-style: none;
    color: var(--text-light);
    font-size: 11px;
  }
  .contact-list li {
    display: flex;
    align-items: center;
    height: 15px;
  }
  .contact-list svg { margin-right: 13px; }
  .address {
    position: absolute;
    left: 283px;
    top: 182px;
    display: flex;
    color: var(--text-light);
    font-size: 11px;
    line-height: 16px;
  }
  .address svg { margin-right: 7px; margin-top: 1px; }
</style>
</head>
<body>
<div class="canvas">

  <section class="card card--front">
    <div class="brand">
      <span class="brand__dot"></span>
      <span class="brand__name">HARROWFIELD</span>
    </div>
  </section>

  <section class="card card--back">
    <svg class="card__band" viewBox="0 0 430 90" aria-hidden="true">
      <path d="M0 0 H430 V62 C380 72 320 70 250 46 C170 20 80 28 0 52 Z" fill="var(--brand-green)"/>
      <path d="M0 52 C80 28 170 20 250 46 C170 26 80 34 0 62 Z" fill="var(--card-dark)"/>
      <path d="M0 62 C80 34 170 26 250 46 C170 32 80 44 0 74 Z" fill="var(--light-green)"/>
    </svg>
    <div class="holder">
      <div class="holder__name">NAME</div>
      <div class="holder__title">Designation</div>
    </div>
    <div class="brand">
      <span class="brand__dot"></span>
      <span class="brand__name">HARROWFIELD</span>
    </div>
    <ul class="contact-list">
      <li><svg width="10" height="10" viewBox="0 0 10 10" aria-hidden="true"><circle cx="5" cy="5" r="5" fill="var(--brand-green)"/><path d="M3 3.2 Q3 7 6.8 7" stroke="var(--card-dark)" stroke-width="1.3" fill="none"/></svg>Phone No.</li>
      <li><svg width="10" height="10" viewBox="0 0 10 10" aria-hidden="true"><circle cx="5" cy="5" r="5" fill="var(--brand-green)"/><rect x="2.6" y="3.4" width="4.8" height="3.2" fill="none" stroke="var(--card-dark)" stroke-width="0.9"/></svg>Email Id</li>
      <li><svg width="10" height="10" viewBox="0 0 10 10" aria-hidden="true"><circle cx="5" cy="5" r="4.4" fill="none" stroke="var(--brand-green)" stroke-width="1.2"/><path d="M0.8 5 H9.2 M5 0.8 V9.2" stroke="var(--brand-green)" stroke-width="0.9"/></svg>Web Address</li>
    </ul>
    <div class="address">
      <svg width="10" height="14" viewBox="0 0 10 14" aria-hidden="true"><path d="M5 0 C2.2 0 0 2.2 0 5 C0 8.5 5 14 5 14 C5 14 10 8.5 10 5 C10 2.2 7.8 0 5 0 Z" fill="var(--brand-green)"/><circle cx="5" cy="5" r="1.8" fill="var(--card-dark)"/></svg>
      <span>42 Lantern Row,<br>Millbrook District</span>
    </div>
  </section>

</div>
</body>
</html>
```